cosmetics need shampoo label of first product (hopefully many more to follow)

we are starting this new project with the creation of the first of a range of shampoos: Design of facing comprehend creation of logo and facing of the product, we want to achieve a brand recognition and facing that makes our product and product stand out, see briefing attached.

We want to have a degree of personality but also give a tone of professional brand.

If project takes off, then more product to design and more resources available.

Target Market(s)

consumer looking for a professional shampoo but not at hairdresser at convenient price and size (1 litre with pump) bottle of white plastic

Industry/Entity Type

Cosmetics

Colors
00a990

Requirements
Must have
• as this shampoo is for damaged hair, green colour is the one that symbolise this category see Velunore Fortique
• we want that the bottle stand out from the crowd and that people get that is a professional brand so the logo neoVita must be seen and the colour most make a difference in the shelves
Nice to have
• good balance between some personality and & professional
• not too white (as will not stand out in white products shelve) but not too colour as they may then merchandise in the shelve with coloured product
• big fonts easy to read
Should not have
• too clinical, to boring,

```html
<!DOCTYPE html>
<html lang="en">
<head>
<meta charset="utf-8">
<title>Neovita Repair Shampoo Label</title>
<link rel="stylesheet" href="https://fonts.googleapis.com/css2?family=Cinzel:wght@400;500&display=swap">
<style>
  :root {
    --page: #ffffff;
    --label-green: #55cc7b;
    --pattern-green: #7ad897;
    --text-green: #3a9a55;
    --white: #ffffff;
    --ink: #111111;
  }
  * { margin: 0; padding: 0; box-sizing: border-box; }
  html, body {
    width: 1000px;
    height: 1200px;
    overflow: hidden;
    background: var(--page);
  }
  .canvas {
    position: relative;
    width: 1000px;
    height: 1200px;
    font-family: "Cinzel", serif;
  }
  .label {
    position: absolute;
    left: 108px;
    top: 80px;
    width: 785px;
    height: 1047px;
    background: var(--label-green);
    overflow: hidden;
  }
  .brand-name {
    position: absolute;
    left: 0;
    width: 100%;
    top: 78px;
    text-align: center;
    color: var(--white);
    font-weight: 400;
    font-size: 72px;
    line-height: 1;
    letter-spacing: 14px;
    text-transform: uppercase;
  }
  .brand-tagline {
    position: absolute;
    left: 0;
    width: 100%;
    top: 170px;
    text-align: center;
    color: var(--white);
    font-size: 34px;
    line-height: 40px;
    letter-spacing: 2px;
  }
  .pattern-band {
    position: absolute;
    left: 0;
    width: 100%;
    background: var(--pattern-green);
  }
  .pattern-band--top { top: 222px; height: 140px; }
  .pattern-band--bottom { top: 875px; height: 172px; }
  .product-panel {
    position: absolute;
    left: 14px;
    top: 365px;
    width: 758px;
    height: 383px;
    background: var(--white);
    border-radius: 72px;
    padding: 32px 0 0 81px;
    color: var(--text-green);
    font-size: 44px;
    line-height: 54px;
    letter-spacing: 3px;
  }
  .product-name + .product-name { margin-top: 54px; }
  .hair-type {
    position: absolute;
    left: 60px;
    top: 776px;
    color: var(--white);
    font-size: 36px;
    line-height: 40px;
    letter-spacing: 1.5px;
  }
  .claims-panel {
    position: absolute;
    left: 84px;
    top: 925px;
    width: 616px;
    height: 93px;
    background: var(--white);
    border-radius: 46px;
    text-align: center;
  }
  .claims {
    margin-top: 10px;
    color: var(--text-green);
    font-size: 26px;
    line-height: 36px;
    letter-spacing: 0.5px;
  }
  .net-content {
    margin-top: 9px;
    color: var(--ink);
    font-size: 25px;
    line-height: 34px;
    font-weight: 500;
  }
</style>
</head>
<body>
<div class="canvas">
  <div class="label">
    <div class="pattern-band pattern-band--top" role="img" aria-label="Decorative band of interlaced white curves"></div>
    <div class="pattern-band pattern-band--bottom" role="img" aria-label="Decorative band of interlaced white curves"></div>

    <h1 class="brand-name">Neovita</h1>
    <p class="brand-tagline">SALON FORMULA</p>

    <div class="product-panel">
      <p class="product-name">Repair shampoo<br>With argan oil</p>
      <p class="product-name" lang="fr">Shampooing<br>reparateur avec huile<br>argain</p>
    </div>

    <p class="hair-type">For weakened – damaged hair<br><span lang="fr">Pour cheveux habimes et affaiblis</span></p>

    <div class="claims-panel">
      <p class="claims">Parabens free – sls free – colour safe</p>
      <p class="net-content">NET WT 33.8 fl oz e 1000 ml</p>
    </div>
  </div>
</div>
</body>
</html>
```